Wedding Day Custom Wine Label - Tasmanian (Tamar Valley) wine

I am looking for a custom design that will be put on a wine label to commemorate a very good friend's wedding day.

We will need to be able to take the design and print it on to sticker labels that we can put on to wine bottles.

The bride and groom have asked for a simplistic label design (see example image attached). We need two labels. One for "Pinot Noir" wine and the other for "Chardonnay" wine. We would like the label to say:

The Hartwell's
Pinot Noir
2023
Tamar Valley

and for for the other wine variety:

The Hartwell's
Chardonnay
2023
Tamar Valley

smaller text below to say:

13.5% ALC/VOL 750ML
MEGAN & LIAM - 31.10.2024

I am happy to consider other variations - the bride & groom would prefer something minimalistic. Elegant and classy.

Target Market(s)

the bride & groom

Requirements
Must have
• Wedding date (31.10.2024). Wine type (Pinot Noir or Chardonnay).
Should not have
• images not essential

```html
<!DOCTYPE html>
<html lang="en">
<head>
<meta charset="utf-8">
<title>The Hartwell's Wedding Wine Labels</title>
<link href="https://fonts.googleapis.com/css2?family=Cabin:wght@500;600&display=swap" rel="stylesheet">
<style>
  :root {
    --backdrop: #000000;
    --label-paper: #ffffff;
    --label-edge: #8a8a8a;
    --ink: #2f2f2f;
    --ink-reverse: #ffffff;
  }
  * { margin: 0; padding: 0; box-sizing: border-box; }
  html, body {
    width: 1200px;
    height: 411px;
    overflow: hidden;
    background: var(--backdrop);
  }
  .label-sheet {
    position: relative;
    width: 1200px;
    height: 411px;
    background: var(--backdrop);
  }
  .wine-label {
    position: absolute;
    top: 65px;
    width: 221px;
    height: 275px;
    background: var(--label-paper);
    border: 1px solid var(--label-edge);
    color: var(--ink);
    font-family: "Cabin", sans-serif;
    text-align: center;
  }
  .wine-label--pinot { left: 370px; }
  .wine-label--chardonnay { left: 615px; }

  .brand-mark {
    position: absolute;
    top: 31px;
    left: 0;
    right: 0;
    display: flex;
    align-items: center;
    justify-content: center;
    gap: 5px;
    font-weight: 600;
    font-size: 11px;
    line-height: 14px;
    letter-spacing: 0.08em;
  }
  .brand-mark__dot {
    width: 9px;
    height: 9px;
    border-radius: 50%;
    background: var(--ink);
  }

  .wine-title {
    position: absolute;
    top: 88px;
    left: 0;
    right: 0;
    font-weight: 500;
    font-size: 21px;
    line-height: 24.5px;
    letter-spacing: 0.03em;
    text-transform: uppercase;
  }
  .wine-title span { display: block; }

  .wine-details {
    position: absolute;
    top: 277px;
    top: 211px;
    left: 0;
    right: 0;
    font-weight: 500;
    font-size: 7.5px;
    letter-spacing: 0.02em;
  }

  .couple-band {
    position: absolute;
    top: 223px;
    left: 50%;
    transform: translateX(-50%);
    width: 88px;
    height: 14px;
  }
  .couple-band__stroke {
    position: absolute;
    inset: 0;
    width: 88px;
    height: 14px;
  }
  .couple-band__stroke polygon { fill: var(--ink); }
  .couple-band__names {
    position: relative;
    color: var(--ink-reverse);
    font-weight: 500;
    font-size: 8.5px;
    line-height: 14px;
    letter-spacing: 0.04em;
  }

  .wedding-date {
    position: absolute;
    top: 241px;
    left: 0;
    right: 0;
    font-weight: 500;
    font-size: 9px;
    letter-spacing: 0.03em;
  }
</style>
</head>
<body>
  <main class="label-sheet">
    <section class="wine-label wine-label--pinot" aria-label="Pinot Noir label">
      <div class="brand-mark"><span class="brand-mark__dot"></span>WILLOWBANK</div>
      <h1 class="wine-title">
        <span>The Hartwell's</span>
        <span>Pinot Noir</span>
        <span>2023</span>
        <span>Tamar Valley</span>
      </h1>
      <p class="wine-details">13.5% ALC/VOL 750 mL</p>
      <div class="couple-band">
        <svg class="couple-band__stroke" viewBox="0 0 88 14" role="img" aria-label="Brush stroke behind the couple's names">
          <polygon points="2,2 86,0 84,7 87,13 4,14 0,8"/>
        </svg>
        <p class="couple-band__names">MEGAN &amp; LIAM</p>
      </div>
      <p class="wedding-date">31.10.2024</p>
    </section>

    <section class="wine-label wine-label--chardonnay" aria-label="Chardonnay label">
      <div class="brand-mark"><span class="brand-mark__dot"></span>WILLOWBANK</div>
      <h1 class="wine-title">
        <span>The Hartwell's</span>
        <span>Chardonnay</span>
        <span>2023</span>
        <span>Tamar Valley</span>
      </h1>
      <p class="wine-details">13.5% ALC/VOL 750 mL</p>
      <div class="couple-band">
        <svg class="couple-band__stroke" viewBox="0 0 88 14" role="img" aria-label="Brush stroke behind the couple's names">
          <polygon points="2,2 86,0 84,7 87,13 4,14 0,8"/>
        </svg>
        <p class="couple-band__names">MEGAN &amp; LIAM</p>
      </div>
      <p class="wedding-date">31.10.2024</p>
    </section>
  </main>
</body>
</html>
```